Fahrzeugbeschriftung für Brandschutzservice
Zielgruppe
Siehe bitte www.lorventa.de
Aufgabenstellung
Brandschutzservice / Kundendienst / Feuerlöscher vor Ort beim Kunden prüfen /

```html
<!DOCTYPE html>
<html lang="de">
<head>
<meta charset="utf-8">
<title>Lorventa GmbH – Fahrzeugbeschriftung</title>
<link href="https://fonts.googleapis.com/css2?family=Courier+Prime:wght@400;700&display=swap" rel="stylesheet">
<style>
  :root {
    --canvas: #f2f3f4;
    --van-white: #ffffff;
    --ink: #1a1a1a;
    --signal-red: #c8201e;
    --flame-deep: #8a1a0c;
    --flame-mid: #e0451a;
    --flame-hot: #f59a1c;
    --flame-glow: #ffd23a;
    --band: rgba(40, 18, 12, 0.78);
    --text-light: #ffffff;
  }
  * { margin: 0; padding: 0; box-sizing: border-box; }
  html, body {
    width: 1200px; height: 800px; overflow: hidden;
    background: var(--canvas);
  }
  .canvas {
    position: relative; width: 1200px; height: 800px;
    font-family: "Courier Prime", "Courier New", monospace;
  }
  .panel {
    position: absolute; left: 60px; top: 60px;
    width: 1080px; height: 680px;
    background: var(--van-white);
    border-radius: 10px;
  }
  .flame-banner {
    position: absolute; left: 100px; top: 130px;
    width: 1000px; height: 276px;
    border-radius: 14px; overflow: hidden;
    background:
      radial-gradient(ellipse at 55% 35%, var(--flame-glow) 0%, transparent 45%),
      radial-gradient(ellipse at 85% 60%, var(--flame-hot) 0%, transparent 55%),
      linear-gradient(100deg, var(--flame-deep) 0%, var(--flame-mid) 30%, var(--flame-hot) 60%, var(--flame-mid) 85%, var(--flame-deep) 100%);
  }
  .brand {
    position: absolute; right: 34px; top: 26px;
    display: flex; align-items: center; gap: 16px;
  }
  .brand-mark {
    width: 30px; height: 30px; background: var(--text-light);
  }
  .brand-name {
    color: var(--text-light); font-weight: 700;
    font-size: 60px; line-height: 1; letter-spacing: 1px;
  }
  .former-name {
    position: absolute; right: 36px; top: 108px;
    color: var(--text-light); font-weight: 700; font-size: 19px;
  }
  .service-band {
    position: absolute; left: 255px; right: 8px; top: 154px; height: 72px;
    background: var(--band);
    display: flex; flex-direction: column; justify-content: center; align-items: center;
    color: var(--text-light); font-weight: 700; font-size: 23px; line-height: 1.4;
  }
  .contact {
    position: absolute; left: 150px; top: 500px;
    text-align: center; font-weight: 700; color: var(--ink);
    font-size: 42px; line-height: 1.3;
  }
  .contact .phone { color: var(--signal-red); }
</style>
</head>
<body>
<main class="canvas">
  <div class="panel"></div>
  <section class="flame-banner" role="img" aria-label="Foto lodernder Flammen als Hintergrund">
    <div class="brand">
      <span class="brand-mark"></span>
      <span class="brand-name">Lorventa GmbH</span>
    </div>
    <p class="former-name">ehemalige Firma: Saaletaler Brandschutzservice</p>
    <div class="service-band">
      <span>Brandschutzservice / Kundendienst</span>
      <span>Feuerlöscher vor Ort beim Kunden prüfen</span>
    </div>
  </section>
  <div class="contact">
    <p>Tel: <span class="phone">03641 57192</span></p>
    <p>lorventa.de</p>
  </div>
</main>
</body>
</html>
```